We need a flyer (size Din A4, folded, see image).
Attached you will find the content with a rough arrangement.
The inner part will contain some Q&A, we have sketched two possible arrangements of the content.
We are looking for a professional design and a good, clean layout.
Maybe you have some ideas how to arrange the content in a smarter way, we are open for suggestions.
The draft contains no images. It would be good to have an explaining image at least on the front of the flyer.
Attached you will find some stock photos we are using on our website, but you can also propose your own images.
If useful, here is our webpage:
https://vorn-strom.de/
and the landing page for the offering
https://vorn-strom. en/charging-solutions-for-house-management-and-routes/
(this landing page is not professionally designed, so feel free to create a better design for the flyer)
Our target group are real estate managers/facility managers of larger apartment buildings.
The offering is: full-serviced solutions for charging infrastructure for electric cars at the parking lots for residents.
Please do not hesitate to contact me, if you need further information.
Target Market(s)
Professionals in real estate management, facility management
Industry/Entity Type
charging infrastructures for electric cars, focus: appartment buildings

```html
<!DOCTYPE html>
<html lang="de">
<head>
<meta charset="utf-8">
<title>vorn-strom – Faltflyer</title>
<link href="https://fonts.googleapis.com/css2?family=Anton&family=Montserrat:wght@400;500;600;700&display=swap" rel="stylesheet">
<style>
:root{
  --ink:#1b1b26;
  --ink-2:#262633;
  --pink:#e8169b;
  --purple:#7b55d6;
  --violet:#9a7ee8;
  --paper:#ffffff;
  --stage:#e4e4e6;
  --text-dark:#202028;
  --muted:#55555f;
  --rule:#d9d9de;
}
*{box-sizing:border-box;margin:0;padding:0}
html,body{width:1200px;height:4000px;overflow:hidden}
body{background:var(--stage);font-family:"Montserrat",sans-serif;position:relative}
.spread{position:absolute;left:45px;width:1110px;height:785px;overflow:hidden;box-shadow:0 6px 24px rgba(0,0,0,.12)}
.spread--outside{top:900px;background:var(--ink)}
.spread--inside{top:2200px;background:var(--paper)}
.spread__art{position:absolute;inset:0;width:1110px;height:785px}
.panel{position:absolute;top:0;height:785px;width:370px}
.panel--1{left:0}.panel--2{left:370px}.panel--3{left:740px}

/* outside – panel 1 */
.offer{padding:44px 34px 0 34px;color:#fff}
.offer__title{color:var(--pink);font-weight:700;font-size:16px;line-height:1.3}
.ticks{list-style:none;margin-top:10px}
.ticks li{display:flex;align-items:center;gap:7px;font-size:10.5px;font-weight:600;margin-bottom:14px}
.tick{width:10px;height:10px;flex:none}
.offer__point{font-size:10px;font-weight:600;line-height:1.4;padding:12px 0;border-bottom:1px solid var(--pink);width:250px}
.offer__point:first-of-type{padding-top:2px}

/* outside – panel 2 */
.contact{text-align:center;color:#fff;padding-top:330px}
.brand{display:inline-flex;align-items:center;gap:8px;font-weight:500;font-size:19px;color:#fff}
.brand__dot{width:14px;height:14px;border-radius:50%;background:var(--pink)}
.contact__lead{font-size:12px;font-weight:600;margin-top:30px;line-height:1.35}
.pill{display:inline-block;background:var(--purple);color:#fff;font-size:11px;font-weight:600;padding:5px 14px;border-radius:12px;margin-top:10px}
.icon{display:block;margin:16px auto 6px;width:16px;height:16px}
.contact__phone{font-size:17px;font-weight:600;letter-spacing:.5px}
.contact__addr{font-size:12px;font-weight:600;line-height:1.3}
.contact__mail{font-size:12px;font-weight:600}

/* outside – panel 3 */
.cover__brand{position:absolute;top:95px;right:42px}
.cover__title{position:absolute;left:0;right:0;top:555px;text-align:center}
.cover__flex{font-family:"Anton",sans-serif;color:var(--pink);font-size:70px;line-height:1;letter-spacing:1px}
.cover__sub{font-family:"Anton",sans-serif;color:var(--text-dark);font-size:23px;line-height:1.1;margin-top:4px}
.cover__emob{font-family:"Anton",sans-serif;color:var(--purple);font-size:39px;line-height:1.05}
.cover__web{font-size:13px;letter-spacing:2px;color:var(--muted);margin-top:10px;font-weight:500}

/* inside */
.qa__head{position:absolute;top:40px;color:var(--pink);font-weight:700;font-size:14px}
.qa__head--q{left:34px}.qa__head--a{left:376px}
.qa__row{position:absolute;left:34px;width:690px;height:104px;border-bottom:1px solid var(--rule);display:flex;align-items:center}
.qa__row:last-of-type{border-bottom:none}
.qa__q{width:210px;font-size:11.5px;font-weight:700;color:var(--text-dark);line-height:1.35}
.qa__arrow{width:64px;height:22px;flex:none;margin-right:22px}
.qa__a{width:170px;font-size:7.5px;line-height:1.45;color:var(--muted);margin-right:22px}
.steps{position:absolute;left:740px;top:0;width:370px;height:785px;background:var(--ink);padding:38px 34px;color:#fff}
.steps__title{color:var(--pink);font-weight:700;font-size:15px;line-height:1.3}
.steps__group{margin-top:30px}
.steps__num{color:var(--pink);font-weight:700;font-size:12px;margin-bottom:10px}
.steps ul{list-style:none}
.steps li{display:flex;align-items:flex-start;gap:8px;font-size:10px;font-weight:500;margin:0 0 12px 14px;line-height:1.35}
.steps li .tick{margin-top:2px}
</style>
</head>
<body>

<!-- Outside -->
<section class="spread spread--outside">
  <svg class="spread__art" viewBox="0 0 1110 785" aria-hidden="false">
    <defs>
      <linearGradient id="evBlue" x1="0" y1="0" x2="1" y2="1">
        <stop offset="0" stop-color="#cfe2ff"/><stop offset=".45" stop-color="#3d6fe0"/><stop offset="1" stop-color="#1b2a6b"/>
      </linearGradient>
      <linearGradient id="evGrey" x1="0" y1="0" x2="1" y2="1">
        <stop offset="0" stop-color="#b9bcc6"/><stop offset=".5" stop-color="#3a55c9"/><stop offset="1" stop-color="#e9e9ee"/>
      </linearGradient>
    </defs>
    <!-- panel 1 photo -->
    <path role="img" aria-label="Foto: Ladestecker mit blau leuchtendem Ring an einer Ladesäule" d="M95 785 L370 500 V785 Z" fill="url(#evGrey)"/>
    <path d="M70 785 L370 475 L370 500 L95 785 Z" fill="var(--pink)"/>
    <path d="M0 690 L120 640 L60 785 H0 Z" fill="var(--purple)"/>
    <!-- panel 2 top photo -->
    <path role="img" aria-label="Foto: Elektroauto an einer Ladestation" d="M420 0 H740 V240 C650 200 540 110 420 0 Z" fill="url(#evBlue)"/>
    <path d="M300 0 H345 L650 205 L620 212 Z" fill="var(--pink)"/>
    <!-- panel 3 cover photo -->
    <path role="img" aria-label="Foto: Ladestecker mit leuchtendem Ring vor einem Elektroauto" d="M740 0 H1110 V470 H740 Z" fill="url(#evBlue)"/>
    <path d="M740 0 H1110 V150 C1030 150 950 160 900 240 C860 310 820 420 740 470 Z" fill="var(--ink)"/>
    <path d="M740 480 L1110 400 V785 H740 Z" fill="var(--pink)"/>
    <path d="M740 520 L1110 430 V785 H740 Z" fill="var(--paper)"/>
    <path d="M740 640 L790 785 H740 Z" fill="var(--violet)"/>
  </svg>

  <div class="panel panel--1 offer">
    <h2 class="offer__title">Bieten Sie Ihren Bewohnern Lademöglichkeiten für ihre Elektrofahrzeuge –</h2>
    <ul class="ticks">
      <li><svg class="tick" viewBox="0 0 10 10"><path d="M1 5 L4 8 L9 1" stroke="#e8169b" stroke-width="2" fill="none"/></svg>einfach,</li>
      <li><svg class="tick" viewBox="0 0 10 10"><path d="M1 5 L4 8 L9 1" stroke="#e8169b" stroke-width="2" fill="none"/></svg>unkompliziert und</li>
      <li><svg class="tick" viewBox="0 0 10 10"><path d="M1 5 L4 8 L9 1" stroke="#e8169b" stroke-width="2" fill="none"/></svg>zukunftsfähig.</li>
    </ul>
    <p class="offer__point">Zukunftsfähig durch flexibles Abrechnungsmodell für verschiedene Einsatzmöglichkeiten.</p>
    <p class="offer__point">Leichter, schneller Einstieg in das Thema, unkomplizierte und professionelle Abwicklung</p>
    <p class="offer__point" style="border-bottom:none">Aufbau und Betrieb von Ladelösungen speziell für Hausverwaltungen und WEGs</p>
  </div>

  <div class="panel panel--2 contact">
    <div class="brand"><span class="brand__dot"></span>vorn-strom</div>
    <p class="contact__lead">Jetzt Beratungsgespräch<br>anfordern unter:</p>
    <span class="pill">https://vorn-strom.de/WEG</span>
    <svg class="icon" viewBox="0 0 16 16"><path d="M4 1 L6.5 4.5 L5 6.5 C6 8.5 7.5 10 9.5 11 L11.5 9.5 L15 12 L13 15 C7 15 1 9 1 3 Z" fill="#e8169b"/></svg>
    <p class="contact__phone">0341 / 555 20 18</p>
    <svg class="icon" viewBox="0 0 16 16"><path d="M8 1 C4.5 1 3 3.5 3 6 C3 9.5 8 15 8 15 C8 15 13 9.5 13 6 C13 3.5 11.5 1 8 1 Z" fill="#e8169b"/><circle cx="8" cy="6" r="2" fill="#1b1b26"/></svg>
    <p class="contact__addr">vorn-strom GmbH<br>Lindenweg 14<br>04109 Leipzig</p>
    <svg class="icon" viewBox="0 0 16 16"><rect x="1" y="3" width="14" height="10" rx="1" fill="#e8169b"/><path d="M1.5 3.5 L8 9 L14.5 3.5" stroke="#1b1b26" stroke-width="1.3" fill="none"/></svg>
    <p class="contact__mail">info@vorn-strom.de</p>
  </div>

  <div class="panel panel--3">
    <div class="brand cover__brand"><span class="brand__dot"></span>vorn-strom</div>
    <div class="cover__title">
      <div class="cover__flex">FLEXIBLE</div>
      <div class="cover__sub">LADEINFRASTRUKTUREN FÜR DIE</div>
      <div class="cover__emob">ELEKTROMOBILITÄT</div>
      <div class="cover__web">www.vorn-strom.de</div>
    </div>
  </div>
</section>

<!-- Inside -->
<section class="spread spread--inside">
  <h3 class="qa__head qa__head--q">Problem / Fragestellung</h3>
  <h3 class="qa__head qa__head--a">Der Lösungsansatz von vorn-strom</h3>

  <div class="qa__row" style="top:70px">
    <p class="qa__q">Ein Bewohner will eine Wallbox – was tun?</p>
    <svg class="qa__arrow" viewBox="0 0 64 22"><path d="M0 6 H48 V0 L64 11 L48 22 V16 H0 Z" fill="#111"/></svg>
    <p class="qa__a">Wir prüfen die Gegebenheiten vor Ort und zeigen, welche Ladelösung für Ihr Objekt passt – schnell und unverbindlich.</p>
    <p class="qa__a">Anschließend erhalten Sie einen klaren Vorschlag zu Technik, Ablauf und Kosten für die Eigentümerversammlung.</p>
  </div>
  <div class="qa__row" style="top:174px">
    <p class="qa__q">Der Stromanschluss reicht nicht, wenn alle Bewohner eine Wallbox wollen!</p>
    <svg class="qa__arrow" viewBox="0 0 64 22"><path d="M0 6 H48 V0 L64 11 L48 22 V16 H0 Z" fill="#111"/></svg>
    <p class="qa__a">Mit einem intelligenten Last-Management verteilen wir die vorhandene Leistung dynamisch auf alle Ladepunkte.</p>
    <p class="qa__a">Ein teurer Ausbau des Hausanschlusses ist in vielen Fällen nicht nötig.</p>
  </div>
  <div class="qa__row" style="top:278px">
    <p class="qa__q">Sind die Vorabprüfung und der Einbau von Ladeinfrastruktur teuer? Wie überzeugt man die WEG von den Kosten?</p>
    <svg class="qa__arrow" viewBox="0 0 64 22"><path d="M0 6 H48 V0 L64 11 L48 22 V16 H0 Z" fill="#111"/></svg>
    <p class="qa__a">Die Erstprüfung ist für Sie kostenfrei. Ihre Bewohner zahlen nur die Ladepunkte, die sie tatsächlich nutzen.</p>
    <p class="qa__a">Wir liefern übersichtliche Unterlagen, mit denen die WEG eine fundierte Entscheidung treffen kann.</p>
  </div>
  <div class="qa__row" style="top:382px">
    <p class="qa__q">Die Bewohner haben keine fest zugeordneten Stellplätze</p>
    <svg class="qa__arrow" viewBox="0 0 64 22"><path d="M0 6 H48 V0 L64 11 L48 22 V16 H0 Z" fill="#111"/></svg>
    <p class="qa__a">Auch ohne feste Stellplätze ist Laden möglich – über gemeinsam genutzte Ladepunkte.</p>
    <p class="qa__a">Die Abrechnung erfolgt automatisch pro Nutzer über eine persönliche Ladekarte.</p>
  </div>
  <div class="qa__row" style="top:486px">
    <p class="qa__q">Wer kann helfen, eine professionelle und zukunftsfähige Ladeinfrastruktur zu entwickeln?</p>
    <svg class="qa__arrow" viewBox="0 0 64 22"><path d="M0 6 H48 V0 L64 11 L48 22 V16 H0 Z" fill="#111"/></svg>
    <p class="qa__a">Wir sind Ihr Spezialist für Ladeinfrastruktur und begleiten Planung, Installation und Betrieb aus einer Hand.</p>
    <p class="qa__a">So bleibt die Anlage mit jedem neuen Nutzer erweiterbar und zukunftssicher.</p>
  </div>
  <div class="qa__row" style="top:590px">
    <p class="qa__q">Bei uns wurden bereits Wallboxen von einzelnen Mietern installiert, was nun?</p>
    <svg class="qa__arrow" viewBox="0 0 64 22"><path d="M0 6 H48 V0 L64 11 L48 22 V16 H0 Z" fill="#111"/></svg>
    <p class="qa__a">Bestehende Wallboxen lassen sich in vielen Fällen in ein gemeinsames System einbinden.</p>
  </div>

  <aside class="steps">
    <h3 class="steps__title">Die Schritte zur Ladeinfrastruktur in Ihrem Objekt:</h3>
    <div class="steps__group">
      <p class="steps__num">1. Erstprüfung</p>
      <ul>
        <li><svg class="tick" viewBox="0 0 10 10"><path d="M1 5 L4 8 L9 1" stroke="#e8169b" stroke-width="2" fill="none"/></svg>Machbarkeitsprüfung</li>
        <li><svg class="tick" viewBox="0 0 10 10"><path d="M1 5 L4 8 L9 1" stroke="#e8169b" stroke-width="2" fill="none"/></svg>Abschätzung, Planung nächster Schritte</li>
      </ul>
    </div>
    <div class="steps__group">
      <p class="steps__num">2. Konzeption</p>
      <ul>
        <li><svg class="tick" viewBox="0 0 10 10"><path d="M1 5 L4 8 L9 1" stroke="#e8169b" stroke-width="2" fill="none"/></svg>Planung der Anlage</li>
        <li><svg class="tick" viewBox="0 0 10 10"><path d="M1 5 L4 8 L9 1" stroke="#e8169b" stroke-width="2" fill="none"/></svg>Abstimmung Netzbetreiber</li>
        <li><svg class="tick" viewBox="0 0 10 10"><path d="M1 5 L4 8 L9 1" stroke="#e8169b" stroke-width="2" fill="none"/></svg>Kostenkalkulation</li>
      </ul>
    </div>
    <div class="steps__group">
      <p class="steps__num">3. Installation</p>
      <ul>
        <li><svg class="tick" viewBox="0 0 10 10"><path d="M1 5 L4 8 L9 1" stroke="#e8169b" stroke-width="2" fill="none"/></svg>Installation von Verkabelung und Elektrotechnik</li>
        <li><svg class="tick" viewBox="0 0 10 10"><path d="M1 5 L4 8 L9 1" stroke="#e8169b" stroke-width="2" fill="none"/></svg>Installation der Wallboxen</li>
        <li><svg class="tick" viewBox="0 0 10 10"><path d="M1 5 L4 8 L9 1" stroke="#e8169b" stroke-width="2" fill="none"/></svg>Setup der Abrechnungssysteme</li>
      </ul>
    </div>
    <div class="steps__group">
      <p class="steps__num">4. Betrieb</p>
      <ul>
        <li><svg class="tick" viewBox="0 0 10 10"><path d="M1 5 L4 8 L9 1" stroke="#e8169b" stroke-width="2" fill="none"/></svg>Technischer Betrieb</li>
        <li><svg class="tick" viewBox="0 0 10 10"><path d="M1 5 L4 8 L9 1" stroke="#e8169b" stroke-width="2" fill="none"/></svg>Abrechnung</li>
        <li><svg class="tick" viewBox="0 0 10 10"><path d="M1 5 L4 8 L9 1" stroke="#e8169b" stroke-width="2" fill="none"/></svg>Regelmäßige Wartung (DGUV3)</li>
        <li><svg class="tick" viewBox="0 0 10 10"><path d="M1 5 L4 8 L9 1" stroke="#e8169b" stroke-width="2" fill="none"/></svg>Anmeldung und Verwaltung neuer Nutzer</li>
      </ul>
    </div>
  </aside>
</section>

</body>
</html>
```